Harbor Crest Physician Advising

I need a one-page advertisement that I can email to potential clients.

The target audience is hospital administrators.

I want it to include the logo, as attached. We specialize in Payer Denial Management. We are certified physician advisors with over 80 years combined clinical medicine experience. We have expertise in Utilization Management, Clinical Documentation Integrity, Peer to Peer Appeals and Letter Appeal Management. We win over 60% of our Peer to Peer Appeals with Medicare Advantage plans and over 50% of our first level letters.

We make sure hospitals get paid for the care they provide, I really want to emphasize that we are very effective at overturning insurance payment denials. We also provider other physician advising services. We keep our company small so that our rates are very affordable. Include that references are available.

We need to include: Contact us today, we can improve your revenue. Please 304-555-0183
or email (I will provide this later).

I want it to look professional but not bland, with maybe AI created images of a small group of physicians (mature, white coats, stethoscopes) looking at a spreadsheet on a laptop. a picture of a stack of money setting on a table, with a hand removing part of the money from the stack.

Companies like ours include Quorvix, T7, Pellingham, Car-Nova, and TelvanMD. Their websites may provide ideas.

Target Market(s)

Healthcare administrators who need to improve their hospital revenue

Industry/Entity Type

Healthcare consulting

Font styles to use
Sans Serif

Colors
0094D4
00A9DD
6FCCEA
C7EBF8
E9F6FB
00AB8E
00BBA5
67D7C9
C6EFE9
E9F9F6
FFC000
F8CF3A
FAE287
FDF2CF
FEFAEE
EE7325
F08F49
F5BC92
FAE3D3
FDF4ED
E54698
E96AAD
F1A4CE
F9D9EA
FCEFF6
6B429C
8869AF
B7A5CE
E3DAEB
F3F0F8

Requirements
Must have
• Must include that we are very successful here to appear in Peer to Peer appeals and Letter appeals
Nice to have
• Very easy to read, big bold fonts
Should not have
• I’m very afraid of having a lot of dark blues, combined with dark gold, because it may look like the colors of a health system in my area

```html
<!DOCTYPE html>
<html lang="en">
<head>
<meta charset="utf-8">
<title>Harbor Crest Physician Advising – Flyer</title>
<link href="https://fonts.googleapis.com/css2?family=Poppins:wght@400;500;600;700;800&family=Great+Vibes&family=Oswald:wght@500&display=swap" rel="stylesheet">
<style>
  :root{
    --blue-top:#0d63c4;
    --blue-deep:#0a2d6b;
    --blue-text:#1760c9;
    --green:#6cc230;
    --green-dark:#3f7a1a;
    --green-box-top:#6ab43a;
    --green-box-bottom:#356b17;
    --ink:#1d1d1f;
    --white:#ffffff;
    --page:#e9e9ea;
  }
  *{box-sizing:border-box;margin:0;padding:0}
  html,body{width:985px;height:1200px;overflow:hidden;background:var(--page)}
  body{font-family:'Poppins',sans-serif;color:var(--ink)}
  .flyer{position:relative;width:985px;height:1200px;overflow:hidden;background:var(--white)}
  .layer{position:absolute;left:0;top:0}
  .abs{position:absolute}

  .photo-group{left:420px;top:131px;width:544px;height:560px;border-radius:200px 200px 0 0;
    background:radial-gradient(ellipse at 50% 40%,#f4f1ee 0%,#dfe6ef 45%,rgba(180,200,225,.6) 75%,rgba(13,80,170,0) 100%)}

  .hero-title{left:89px;top:62px;color:var(--white);font-weight:400;font-size:48px;line-height:1}
  .hero-main{left:86px;top:118px;color:var(--green);font-weight:700;font-size:76px;line-height:1;letter-spacing:-1px}
  .hero-script{left:92px;top:192px;color:var(--white);font-family:'Great Vibes',cursive;font-size:88px;line-height:1}
  .hero-rule{left:89px;top:299px;width:371px;height:1.5px;background:rgba(255,255,255,.85)}

  .feature{left:89px;display:flex;gap:10px;font-weight:600;font-size:25px;line-height:1.2;color:var(--white)}
  .feature .tick{flex:0 0 26px;height:26px;margin-top:2px}
  .feature .accent{color:var(--green)}
  .feature-1{top:332px}
  .feature-2{top:410px}

  .badge{left:437px;top:531px;width:160px;height:160px}
  .badge-text{left:437px;top:561px;width:160px;text-align:center;color:var(--white);font-weight:700;font-size:19px;line-height:1.3}

  .heading{left:89px;color:var(--blue-text);font-weight:700;font-size:19.5px;line-height:1.25;text-transform:uppercase}
  .h-specialize{top:582px}
  .h-paid{top:646px}
  .h-cost{top:762px}

  .money{left:89px;top:672px;width:74px;height:50px;border-radius:4px;background:linear-gradient(135deg,#d8e3cf,#9fb894)}
  .money-text{left:171px;top:676px;font-size:15px;line-height:1.35}
  .dash{height:0;border-top:1px dashed #9a9a9a}
  .dash-left{left:89px;top:740px;width:315px}

  .stat{left:89px;display:flex;align-items:center;gap:8px}
  .stat-num{display:flex;align-items:baseline;white-space:nowrap;flex:0 0 auto;color:var(--green-dark);line-height:1}
  .stat-num .digits{font-family:'Oswald',sans-serif;font-weight:500;font-size:40px;letter-spacing:-1.5px}
  .stat-num .plus{font-family:'Poppins',sans-serif;font-size:28px;font-weight:500;margin-left:2px}
  .stat-text{font-size:15.5px;line-height:1.3;white-space:nowrap}
  .stat-1{top:831px}
  .stat-2{top:898px}
  .tagline{left:89px;top:957px;font-size:15.5px;line-height:1.35}

  .best-title{left:574px;top:684px;color:var(--white);font-weight:700;font-size:19.5px}
  .best-list{left:583px;top:729px;list-style:none;color:var(--white);font-size:16px;line-height:1.1}
  .best-list li{display:flex;gap:9px;align-items:flex-start;margin-bottom:15px}
  .best-list .dot{flex:0 0 10px;height:10px;margin-top:5px;border-radius:50%;background:#7fc8ee}

  .brand{left:89px;top:1080px;width:211px;text-align:center}
  .brand-name{display:flex;align-items:center;justify-content:center;gap:8px;font-weight:700;font-size:22px;color:var(--ink);letter-spacing:-.3px}
  .brand-name .mark{width:14px;height:14px;border-radius:50%;background:var(--blue-text)}
  .brand-sub{font-weight:600;font-size:11.5px;letter-spacing:.4px;margin-top:2px}

  .small-team{left:339px;top:1026px;font-size:19px;line-height:1.25}
  .small-team b{font-weight:700}
  .small-team .blue{color:var(--blue-text);font-weight:700}
  .perk{top:1028px;display:flex;gap:4px;font-size:16.5px;line-height:1.3}
  .perk .ck{flex:0 0 10px;height:10px;margin-top:6px}
  .perk-1{left:534px}
  .perk-2{left:623px}
  .perk-3{left:762px}
  .dash-bottom{left:339px;top:1085px;width:559px;border-top-color:#b5b5b5}

  .contact-cta{left:339px;top:1094px;font-weight:700;font-size:22px;line-height:1.2}
  .contact-cta .blue{color:var(--blue-text)}
  .contact-cta .green{color:var(--green-dark)}
  .contact-line{left:638px;display:flex;align-items:center;gap:8px;font-size:16px}
  .contact-line svg{width:16px;height:16px}
  .contact-phone{top:1097px}
  .contact-mail{top:1124px}

  .foot-bar{left:0;top:1190px;width:985px;height:10px;background:var(--green-dark)}
</style>
</head>
<body>
<main class="flyer">
  <svg class="layer" width="985" height="1200" viewBox="0 0 985 1200" aria-hidden="true">
    <defs>
      <linearGradient id="skyGradient" x1="0" y1="0" x2="0" y2="1">
        <stop offset="0" stop-color="#0d63c4"/>
        <stop offset="1" stop-color="#0a2d6b"/>
      </linearGradient>
    </defs>
    <rect width="985" height="720" fill="url(#skyGradient)"/>
  </svg>

  <div class="abs photo-group" role="img" aria-label="Photo of three smiling physicians in white coats with stethoscopes, one holding a laptop and one holding cash"></div>

  <svg class="layer" width="985" height="1200" viewBox="0 0 985 1200" aria-hidden="true">
    <defs>
      <linearGradient id="boxGradient" x1="0" y1="0" x2="0" y2="1">
        <stop offset="0" stop-color="#6ab43a"/>
        <stop offset="1" stop-color="#356b17"/>
      </linearGradient>
    </defs>
    <path d="M0 459 C150 490 320 540 440 588 L440 620 L0 620 Z" fill="#6cc230"/>
    <path d="M0 566 C150 505 300 530 440 588 C480 630 510 680 536 700 L536 720 L0 720 Z" fill="#ffffff"/>
    <path d="M985 590 C960 640 930 678 890 700 L985 700 Z" fill="#ffffff"/>
    <rect y="700" width="985" height="500" fill="#ffffff"/>
    <path d="M430 578 C520 650 620 668 720 668 C800 668 860 660 898 646 L898 982 Q898 992 888 992 L546 992 Q536 992 536 982 L536 700 C500 650 466 610 430 578 Z" fill="url(#boxGradient)"/>
  </svg>

  <h1 class="abs hero-title">Harbor Crest</h1>
  <div class="abs hero-main">Physician</div>
  <div class="abs hero-script">Advising</div>
  <div class="abs hero-rule"></div>

  <div class="abs feature feature-1">
    <svg class="tick" viewBox="0 0 26 26"><circle cx="13" cy="13" r="13" fill="#4f9e2a"/><path d="M7.5 13.5l4 4 7-8" fill="none" stroke="#0a2d6b" stroke-width="2.6" stroke-linecap="round" stroke-linejoin="round"/></svg>
    <span>Certified Physician<br>Advisors</span>
  </div>
  <div class="abs feature feature-2">
    <svg class="tick" viewBox="0 0 26 26"><circle cx="13" cy="13" r="13" fill="#4f9e2a"/><path d="M7.5 13.5l4 4 7-8" fill="none" stroke="#0a2d6b" stroke-width="2.6" stroke-linecap="round" stroke-linejoin="round"/></svg>
    <span><span class="accent">80+ Years of</span><br>Clinical Experience</span>
  </div>

  <svg class="abs badge" viewBox="0 0 180 180" aria-hidden="true">
    <polygon fill="#1760c9" points="172,90 161.5,109.2 161,131 142.3,142.3 131,161 109.2,161.5 90,172 70.8,161.5 49,161 37.7,142.3 19,131 18.5,109.2 8,90 18.5,70.8 19,49 37.7,37.7 49,19 70.8,18.5 90,8 109.2,18.5 131,19 142.3,37.7 161,49 161.5,70.8"/>
    <circle cx="90" cy="90" r="68" fill="none" stroke="#ffffff" stroke-width="1.2" stroke-dasharray="3 3"/>
  </svg>
  <div class="abs badge-text">Let’s<br>Recover<br>Your<br>Revenue</div>

  <h2 class="abs heading h-specialize">We specialize in payer<br>denial management</h2>
  <h2 class="abs heading h-paid">We help hospitals get paid</h2>
  <div class="abs money" role="img" aria-label="Photo of a stack of dollar bills"></div>
  <p class="abs money-text">Insurance denials cost your<br>hospital money.</p>
  <div class="abs dash dash-left"></div>

  <h2 class="abs heading h-cost">Insurance denials cost your<br>hospital money</h2>
  <div class="abs stat stat-1">
    <span class="stat-num"><span class="digits">60%</span><span class="plus">+</span></span>
    <span class="stat-text">Success rate in Peer-to-Peer<br>appeals (Medicare Advantage)</span>
  </div>
  <div class="abs stat stat-2">
    <span class="stat-num"><span class="digits">50%</span><span class="plus">+</span></span>
    <span class="stat-text">Success rate in First-Level<br>Letter Appeals</span>
  </div>
  <p class="abs tagline">Affordable, physician-led services<br>tailored to your needs</p>

  <h2 class="abs best-title">WHAT WE DO BEST</h2>
  <ul class="abs best-list">
    <li><span class="dot"></span><span>Peer-to-Peer Appeals</span></li>
    <li><span class="dot"></span><span>Overturning insurance<br>payment denials</span></li>
    <li><span class="dot"></span><span>Letter Appeal Management</span></li>
    <li><span class="dot"></span><span>Utilization Management (UM)</span></li>
    <li><span class="dot"></span><span>Clinical Documentation<br>Integrity (CDI)</span></li>
    <li><span class="dot"></span><span>Physician Advising Services</span></li>
  </ul>

  <div class="abs brand">
    <div class="brand-name"><span class="mark"></span><span>HARBOR CREST</span></div>
    <div class="brand-sub">PHYSICIAN ADVISING</div>
  </div>

  <p class="abs small-team">WE’RE A <b>SMALL</b><br><span class="blue">EXPERT TEAM</span></p>
  <div class="abs perk perk-1"><svg class="ck" viewBox="0 0 10 10"><circle cx="5" cy="5" r="5" fill="#4f9e2a"/><path d="M2.8 5.2l1.5 1.5 2.9-3" fill="none" stroke="#fff" stroke-width="1.2"/></svg><span>Lower<br>&nbsp;rates</span></div>
  <div class="abs perk perk-2"><svg class="ck" viewBox="0 0 10 10"><circle cx="5" cy="5" r="5" fill="#4f9e2a"/><path d="M2.8 5.2l1.5 1.5 2.9-3" fill="none" stroke="#fff" stroke-width="1.2"/></svg><span>Faster<br>turnaround</span></div>
  <div class="abs perk perk-3"><svg class="ck" viewBox="0 0 10 10"><circle cx="5" cy="5" r="5" fill="#4f9e2a"/><path d="M2.8 5.2l1.5 1.5 2.9-3" fill="none" stroke="#fff" stroke-width="1.2"/></svg><span>Personalized<br>service</span></div>
  <div class="abs dash dash-bottom"></div>

  <p class="abs contact-cta"><span class="blue">CONTACT US TODAY!</span><br><span class="green">References available</span></p>
  <div class="abs contact-line contact-phone">
    <svg viewBox="0 0 16 16" aria-hidden="true"><circle cx="8" cy="8" r="8" fill="#1a3f94"/><path d="M5.3 4.2l1.4 1.6-.8 1c.5 1 1.3 1.8 2.3 2.3l1-.8 1.6 1.4-.7 1.3c-2.9-.4-5.1-2.6-5.5-5.5z" fill="#fff"/></svg>
    <span>304-555-0183</span>
  </div>
  <div class="abs contact-line contact-mail">
    <svg viewBox="0 0 16 16" aria-hidden="true"><circle cx="8" cy="8" r="8" fill="#1a3f94"/><rect x="4" y="5.3" width="8" height="5.6" rx=".6" fill="#fff"/><path d="M4.3 5.6L8 8.5l3.7-2.9" fill="none" stroke="#1a3f94" stroke-width=".9"/></svg>
    <span>hello@harborcrestadvising.com</span>
  </div>

  <div class="abs foot-bar"></div>
</main>
</body>
</html>
```